lunetra.com redesign

We are a successful web hosting company that has been around since 1999 with 10,000 customers managing 2,000 websites and 12,000 domain names. Our challenge - we are losing ground because our site is getting old, our pricing is not competitive and our feature set needs to change to match the new world of mobile centric everything. We want to reach out to all of the domain names that we don't host websites for. We believe that if we designed a new site that focuses on bringing home all of those externally hosted websites to our own web hosting company that we would have a solid future. We need to compete against mopwizzle.com, vantrimble.com, kerbloom.com, zinqhut.com, nolvark.com, brimfolk.com, quorvane.com, welbix.com and 100,000 others. We need to simplify our message with clean design, focused pages, easy decision making processes for the consumer. We use WHMCS for the background provisioning and billing so we can pretty much manage any kind of pricing model and discounted promotion packages.
I would prefer Twitter bootstrap CSS based responsive design.

Reason: I was away on vacation for 2 weeks - I just got back - I need time to fairly review all submissions - thank you for your patience. Dorian Fenwick Lunetra.com

Thanks to all who submitted sample designs - unfortunately most of them were nothing much more than already available templates with some of my current content and logo added to them. I will try to be more specific to reduce the number of choices. I need the template be fully compatible with WHMCS and Wordpress if you can't make it work with WHMCS directly. Another question I have to ask is -"exactly what am I getting for my $500.00 - is it just a PSD template or actual integration of that theme into WHMCS or Wordpress?"  I don't expect anyone to create new content for the site at that price. What do you charge if  you are able to create content or get directly involved in the site implementation of that template?

```html
<!DOCTYPE html>
<html lang="en">
<head>
<meta charset="utf-8">
<title>Lunetra – Web Hosting</title>
<link rel="stylesheet" href="https://fonts.googleapis.com/css2?family=Ubuntu:wght@400;500;700&family=Titillium+Web:ital,wght@1,600;1,700&family=Roboto+Condensed:wght@700&display=swap">
<style>
:root{
  --hero-a:#1d5f7e; --hero-b:#3a9dbb; --hero-c:#7fd0e3;
  --bar:#111315; --nav-item:#050607;
  --band:#dedede; --page:#f4f4f4; --side:#ececec;
  --text:#333; --muted:#666; --light:#888;
  --accent:#2f9cc4; --accent-dark:#1f6f95; --price:#a71c1c;
  --blogger:#3d5560; --seo:#6a5149; --biz:#141414;
  --foot:#1b1b1b; --foot-text:#6f6f6f; --white:#fff;
}
*{margin:0;padding:0;box-sizing:border-box}
html,body{width:1200px;height:1200px;overflow:hidden}
body{position:relative;background:var(--page);font-family:"Ubuntu",sans-serif;color:var(--text)}
.abs{position:absolute}
.hero{left:0;top:0;width:1200px;height:308px;background:radial-gradient(ellipse at 62% 55%,var(--hero-c) 0%,var(--hero-b) 35%,var(--hero-a) 100%)}
.topbar{left:180px;top:29px;width:858px;height:58px;background:linear-gradient(180deg,#222 0%,var(--bar) 100%)}
.brand{left:18px;top:6px;font:700 40px/1 "Ubuntu",sans-serif;color:var(--white);letter-spacing:-1px}
.nav{right:18px;top:14px;display:flex;gap:4px;list-style:none}
.nav li{background:var(--nav-item);color:var(--white);font:500 12px/32px "Ubuntu",sans-serif;padding:0 11px;height:32px}
.hero-title{left:192px;top:114px;font:italic 700 29px/1 "Titillium Web",sans-serif;color:var(--white)}
.hero-list{left:180px;top:152px;list-style:none;font:italic 600 17px/20px "Titillium Web",sans-serif;color:var(--white)}
.hero-price{left:518px;top:140px;font:italic 700 64px/1 "Titillium Web",sans-serif;color:var(--white);letter-spacing:-3px}
.more{left:577px;top:233px;font:italic 700 15px/1 "Titillium Web",sans-serif;color:var(--white);display:flex;align-items:center;gap:4px}
.dots{left:180px;top:284px;display:flex;gap:6px}
.dots span{width:10px;height:10px;background:#3d8eab}
.dots span.on{background:#5fc1dc}
.servers{left:750px;top:89px;width:278px;height:233px;border-radius:6px;background:linear-gradient(160deg,#5a5e62 0%,#2a2c2e 55%,#111 100%)}
.search-band{left:0;top:308px;width:1200px;height:57px;background:linear-gradient(180deg,#e6e6e6,var(--band))}
.search-label{left:181px;top:331px;font:500 13px/1 "Ubuntu",sans-serif;color:#666}
.field{background:var(--white);border:1px solid #cfcfcf;box-shadow:inset 0 1px 2px rgba(0,0,0,.12)}
.btn{display:flex;align-items:center;justify-content:space-between;padding:0 6px;color:var(--white);font:700 12px/1 "Roboto Condensed",sans-serif;background:linear-gradient(180deg,#46b3d8,var(--accent))}
.btn svg{flex:none}
.sidebar{left:733px;top:365px;width:296px;height:565px;background:var(--side)}
h2.welcome{left:180px;top:385px;font:400 16px/1 "Ubuntu",sans-serif;color:#222}
.intro{left:180px;top:414px;width:540px;font:400 11px/17px "Ubuntu",sans-serif;letter-spacing:.25px;color:var(--muted)}
.plan{top:505px;width:175px;height:204px;background:var(--white)}
.plan h3{height:33px;padding-left:9px;font:500 13.5px/33px "Ubuntu",sans-serif;color:var(--white)}
.plan ul{list-style:none;padding:6px 0 0 9px;font:500 12.5px/23px "Ubuntu",sans-serif;color:#222}
.plan .price{position:absolute;left:9px;top:160px;width:158px;height:36px;background:linear-gradient(180deg,#b52424,var(--price));font-size:15px;padding:0 8px}
.feat{top:747px;width:160px}
.feat h4{font:500 13px/1 "Ubuntu",sans-serif;color:#222;margin-bottom:9px}
.feat li{list-style:none;font:400 10.5px/11px "Ubuntu",sans-serif;color:var(--light);margin-bottom:10px}
.vsep{top:720px;width:1px;height:190px;background:#e3e3e3}
.side-h{font:400 16px/1 "Ubuntu",sans-serif;color:#222}
.side-sub{font:400 12px/1 "Ubuntu",sans-serif;color:#555}
.box{background:var(--white);border:1px solid #e0e0e0}
.lbl{font:400 10.5px/1 "Ubuntu",sans-serif;color:#666}
.footer{left:0;top:930px;width:1200px;height:270px;background:linear-gradient(180deg,#111 0%,var(--foot) 12%)}
.foot-h{top:950px;font:400 16px/1 "Ubuntu",sans-serif;color:#e6e6e6}
.updates{left:180px;top:978px;width:265px;list-style:none;font:400 10.5px/10px "Ubuntu",sans-serif;color:var(--foot-text)}
.updates li{margin-bottom:11px}
.testi{left:466px;top:982px;width:262px;font:400 10.5px/17px "Ubuntu",sans-serif;color:var(--foot-text)}
.testi em{color:#5e5e5e}
.testi b{font-weight:400;color:#8c8c8c}
.contact{left:752px;top:978px;list-style:none;font:500 14px/1 "Ubuntu",sans-serif;color:var(--white)}
.contact li{display:flex;align-items:center;gap:10px;height:38px}
.rule{left:150px;top:1139px;width:900px;height:1px;background:#333}
.legal{left:0;top:1163px;width:1200px;text-align:center;font:400 10.5px/1 "Ubuntu",sans-serif;color:#666}
.legal a{color:#ddd;text-decoration:none}
.legal i{font-style:normal;color:#555;padding:0 4px}
</style>
</head>
<body>

<section class="hero abs">
  <div class="topbar abs">
    <div class="brand abs">lunetra</div>
    <ul class="nav abs">
      <li>HOME</li><li>ABOUT</li><li>DOMAIN NAME</li><li>WEB HOSTING CENTER</li><li>CONTACT</li>
    </ul>
  </div>

  <svg class="abs" style="left:462px;top:136px" width="76" height="76" viewBox="0 0 76 76" aria-hidden="true">
    <circle cx="38" cy="38" r="38" fill="#ffffff" opacity=".18"/>
    <path d="M30 20 L50 38 L30 56" fill="none" stroke="#ffffff" stroke-opacity=".35" stroke-width="10" stroke-linecap="round"/>
  </svg>

  <h1 class="hero-title abs">DOMAIN NAMES FROM</h1>
  <ul class="hero-list abs">
    <li>- Easy transfer</li>
    <li>- Advanced DNS control</li>
    <li>- Personalised email</li>
    <li>- NEW: domain privacy</li>
  </ul>
  <div class="hero-price abs">$3.99</div>
  <div class="more abs">MORE DETAILS
    <svg width="24" height="24" viewBox="0 0 24 24" aria-hidden="true"><circle cx="12" cy="12" r="12" fill="#fff"/><path d="M10 7l5 5-5 5" fill="none" stroke="#3a9dbb" stroke-width="3"/></svg>
  </div>
  <div class="dots abs"><span></span><span></span><span class="on"></span></div>
</section>

<div class="search-band abs"></div>
<div class="servers abs" role="img" aria-label="Stack of rack-mounted hosting servers"></div>

<div class="search-label abs">DOMAIN SEARCH</div>
<div class="field abs" style="left:286px;top:325px;width:164px;height:24px"></div>
<div class="field abs" style="left:460px;top:325px;width:64px;height:24px"></div>
<div class="btn abs" style="left:533px;top:324px;width:86px;height:27px">check
  <svg width="16" height="16" viewBox="0 0 16 16"><circle cx="8" cy="8" r="8" fill="#fff" opacity=".45"/><path d="M7 4.5l3.5 3.5L7 11.5" fill="none" stroke="#fff" stroke-width="2"/></svg></div>
<div class="btn abs" style="left:628px;top:324px;width:86px;height:27px">suggest
  <svg width="16" height="16" viewBox="0 0 16 16"><circle cx="8" cy="8" r="8" fill="#fff" opacity=".45"/><path d="M7 4.5l3.5 3.5L7 11.5" fill="none" stroke="#fff" stroke-width="2"/></svg></div>

<aside class="sidebar abs"></aside>

<main>
  <h2 class="welcome abs">Welcome to LUNETRA</h2>
  <p class="intro abs">Lorem ipsum dolor sit amet, consectetur adipisicing elit, sed do eiusmod tempor incididunt ut l abore et dolore magna aliqua. Ut enim ad minim veniam, quis nostrud exercitation ullamco laboris nisi ut aliquip ex ea commodo consequat. Duis aute irure dolor in reprehenderit in voluptate velit esse cillum dolore eu fugiat nulla pariatur.</p>

  <article class="plan abs" style="left:180px">
    <h3 style="background:var(--blogger)">Blogger</h3>
    <ul><li>100 MB space</li><li>2 GB/mo. transfer</li><li>1 DataNest databases</li><li>1 domain</li><li>10 email</li></ul>
    <div class="btn price">£1.99 / month
      <svg width="16" height="16" viewBox="0 0 16 16"><circle cx="8" cy="8" r="8" fill="#fff" opacity=".45"/><path d="M7 4.5l3.5 3.5L7 11.5" fill="none" stroke="#fff" stroke-width="2"/></svg></div>
  </article>
  <article class="plan abs" style="left:364px">
    <h3 style="background:var(--seo)">SEO pro</h3>
    <ul><li>500 MB space</li><li>5 GB/mo. transfer</li><li>2 DataNest databases</li><li>5 domain + IP</li><li>20 emailboxes</li></ul>
    <div class="btn price">£2.99 / month
      <svg width="16" height="16" viewBox="0 0 16 16"><circle cx="8" cy="8" r="8" fill="#fff" opacity=".45"/><path d="M7 4.5l3.5 3.5L7 11.5" fill="none" stroke="#fff" stroke-width="2"/></svg></div>
  </article>
  <article class="plan abs" style="left:548px">
    <h3 style="background:var(--biz)">Business</h3>
    <ul><li>2000 MB space</li><li>10 GB/mo. transfer</li><li>5 DataNest databases</li><li>Unlimited domains</li><li>Unlimited email</li></ul>
    <div class="btn price">£5.99 / month
      <svg width="16" height="16" viewBox="0 0 16 16"><circle cx="8" cy="8" r="8" fill="#fff" opacity=".45"/><path d="M7 4.5l3.5 3.5L7 11.5" fill="none" stroke="#fff" stroke-width="2"/></svg></div>
  </article>

  <div class="vsep abs" style="left:361px"></div>
  <div class="vsep abs" style="left:543px"></div>

  <section class="feat abs" style="left:189px">
    <h4>Common features</h4>
    <ul><li>No Contracts or Hidden Fees</li><li>30 Day Money Back Guarantee</li><li>24-hour Premium Customer Service</li><li>Reliable and Secure Web Hosting</li><li>Easy-to-use all Design Tools</li></ul>
  </section>
  <section class="feat abs" style="left:371px">
    <h4>Dedicated servers</h4>
    <ul><li>No Contracts or Hidden Fees</li><li>30 Day Money Back Guarantee</li><li>24-hour Premium Customer Service</li><li>Reliable and Secure Web Hosting</li><li>Easy-to-use all Design Tools</li></ul>
  </section>
  <section class="feat abs" style="left:552px">
    <h4>Cloud hosting</h4>
    <ul><li>No Contracts or Hidden Fees</li><li>30 Day Money Back Guarantee</li><li>24-hour Premium Customer Service</li><li>Reliable and Secure Web Hosting</li><li>Easy-to-use all Design Tools</li></ul>
  </section>
</main>

<div class="side-h abs" style="left:744px;top:386px">Existing customers</div>
<div class="side-sub abs" style="left:745px;top:425px">Your account</div>
<div class="box abs" style="left:745px;top:449px;width:277px;height:110px"></div>
<div class="lbl abs" style="left:754px;top:468px">Domain</div>
<div class="field abs" style="left:847px;top:459px;width:164px;height:24px"></div>
<div class="lbl abs" style="left:754px;top:500px">Password</div>
<div class="field abs" style="left:847px;top:491px;width:164px;height:24px"></div>
<div class="btn abs" style="left:847px;top:523px;width:87px;height:27px">LOG IN
  <svg width="16" height="16" viewBox="0 0 16 16"><circle cx="8" cy="8" r="8" fill="#fff" opacity=".45"/><path d="M7 4.5l3.5 3.5L7 11.5" fill="none" stroke="#fff" stroke-width="2"/></svg></div>
<div class="abs" style="left:971px;top:531px;font:700 11px/1 'Roboto Condensed',sans-serif;color:var(--accent-dark)">Reminder</div>

<div class="abs" style="left:744px;top:580px;font:400 12px/1 'Ubuntu',sans-serif;color:#555">Support - <span style="font-size:16px;font-weight:500;color:var(--accent-dark)">24/7/365</span></div>
<p class="abs" style="left:744px;top:609px;width:272px;font:400 10.5px/17px 'Ubuntu',sans-serif;letter-spacing:.2px;color:#666">drop us a line - all those messages has got high prioity, so be resonable</p>
<div class="abs" style="left:744px;top:664px;font:500 12px/1 'Ubuntu',sans-serif;color:var(--accent-dark)">Subimt a ticket</div>
<div class="box abs" style="left:745px;top:688px;width:277px;height:178px"></div>
<div class="lbl abs" style="left:754px;top:707px">Domain / Account</div>
<div class="field abs" style="left:847px;top:698px;width:164px;height:24px"></div>
<div class="lbl abs" style="left:754px;top:739px">Problem</div>
<div class="field abs" style="left:847px;top:731px;width:164px;height:91px"></div>
<div class="btn abs" style="left:847px;top:830px;width:87px;height:27px">SEND
  <svg width="16" height="16" viewBox="0 0 16 16"><circle cx="8" cy="8" r="8" fill="#fff" opacity=".45"/><path d="M7 4.5l3.5 3.5L7 11.5" fill="none" stroke="#fff" stroke-width="2"/></svg></div>

<footer class="footer abs"></footer>
<div class="foot-h abs" style="left:180px">System updates</div>
<ul class="updates abs">
  <li>11/12/2010 1am - New SQL database</li>
  <li>12/12/2010 4am - New hard drive cluster. Increase capacity THREE TIMES.</li>
  <li>13/12/2010 4am - Halyard update - 8min break</li>
  <li>15/12/2010 3am - Security update - 2min break</li>
  <li>16/12/2010 7am - New version of PanelDesk for reseller accounts - update to ver. 7.2</li>
</ul>
<div class="foot-h abs" style="left:466px">Testimonials</div>
<p class="testi abs">So far we've got some happy customers. They share their experience with us:<br>
<em>Lorem ipsum dolor sit amet, consectetur adipisicing elit, sed do.</em><br><b>Big Company</b><br>
<em>Lorem ipsum dolor sit amet, consectetur adipisicing elit, sed do.</em><br><b>Big Company</b></p>
<div class="foot-h abs" style="left:752px">Contact us</div>
<ul class="contact abs">
  <li><svg width="24" height="24" viewBox="0 0 24 24" aria-hidden="true"><path d="M7 3c1 0 2 3 2 4s-2 2-2 3c1 3 3 5 6 6 1 0 2-2 3-2s4 1 4 2-2 4-4 4C9 20 4 15 4 7c0-2 2-4 3-4z" fill="#bbb"/></svg>0800 555 019 2</li>
  <li><svg width="24" height="24" viewBox="0 0 24 24" aria-hidden="true"><rect x="3" y="9" width="18" height="11" rx="2" fill="#8fb6cc"/><rect x="5" y="4" width="14" height="6" rx="3" fill="#ccc"/><rect x="7" y="12" width="10" height="5" fill="#466"/></svg>0900 555 027 4</li>
  <li><svg width="24" height="24" viewBox="0 0 24 24" aria-hidden="true"><rect x="3" y="7" width="18" height="13" rx="1" fill="#ddd"/><path d="M3 7l9 7 9-7" fill="none" stroke="#2a9c4b" stroke-width="2"/></svg>mail@lunetra.com</li>
</ul>
<div class="rule abs"></div>
<div class="legal abs">© 2014 LUNETRA - All right reserved. <a href="#">home</a><i>|</i><a href="#">about</a><i>|</i><a href="#">shared hosting</a><i>|</i><a href="#">dedicated servers</a><i>|</i><a href="#">contact</a></div>

</body>
</html>
```